"Breathe & Bloom" Book Cover 5.5x8.5

Title of the book is "Breathe & Bloom"
Subtitle is "Unmasking Pricing Myths"
I've used PixelGuild on multiple occasions you can look on my Borvex page, Mark Delwitt, to see the covers I've used in the other projects I've done.
The target audience are people who have been tricked to think they can't retire because inflation, i.e. cost of living is going up so much they must work to keep up. There is no evidence of this.
And those are the people I want to reach so they can "Breathe...and Bloom."
Target Market(s)
Americans aged 55 and over who are thinking about retirement
Industry/Entity Type
Financial
Requirements
Nice to have
- Keep It Simple, Stupid is my mantra. Just make it pop out when people are browsing
Should not have
- No piggy banks. No old people sitting on a beach.

```html
<!DOCTYPE html>
<html lang="en">
<head>
<meta charset="utf-8">
<title>Breathe &amp; Bloom — Book Cover</title>
<link href="https://fonts.googleapis.com/css2?family=Cinzel:wght@400;500;600&display=swap" rel="stylesheet">
<style>
  :root {
    --page-bg: #e8e2d8;
    --cover-tan: #bf8a52;
    --band-white: #ffffff;
    --type-white: #ffffff;
    --wood-light: #e8c48e;
    --wood-mid: #d29d5f;
    --wood-dark: #b07a40;
    --text-shadow: rgba(80, 45, 15, 0.28);
  }
  * { margin: 0; padding: 0; box-sizing: border-box; }
  html, body {
    width: 1200px;
    height: 848px;
    overflow: hidden;
    background: var(--page-bg);
  }
  .stage {
    position: relative;
    width: 1200px;
    height: 848px;
  }
  .book-cover {
    position: absolute;
    left: 328px;
    top: 0;
    width: 543px;
    height: 848px;
    background: var(--cover-tan);
    overflow: hidden;
    font-family: "Cinzel", "Trajan Pro", serif;
    color: var(--type-white);
  }
  .photo-band {
    position: absolute;
    left: 0;
    top: 426px;
    width: 100%;
    height: 311px;
    background: var(--band-white);
  }
  .chair-photo {
    position: absolute;
    left: 162px;
    top: 387px;
    width: 214px;
    height: 350px;
    border-radius: 6px 6px 0 0;
    background: linear-gradient(180deg, var(--wood-mid) 0%, var(--wood-light) 45%, var(--wood-dark) 100%);
    opacity: 0.85;
  }
  .cover-line {
    position: absolute;
    left: 0;
    width: 100%;
    text-align: center;
    white-space: nowrap;
    text-shadow: 2px 3px 5px var(--text-shadow);
  }
  .title-top {
    top: 52px;
    font-size: 82px;
    font-weight: 500;
    line-height: 1;
  }
  .title-amp {
    top: 150px;
    font-size: 46px;
    font-weight: 500;
    line-height: 1;
  }
  .title-bottom {
    top: 206px;
    font-size: 100px;
    font-weight: 500;
    line-height: 1;
  }
  .subtitle {
    top: 322px;
    font-size: 17px;
    font-weight: 500;
    letter-spacing: 2.6px;
    line-height: 1;
  }
  .author {
    top: 773px;
    font-size: 30px;
    font-weight: 500;
    letter-spacing: 5px;
    line-height: 1;
  }
</style>
</head>
<body>
  <main class="stage">
    <article class="book-cover">
      <div class="photo-band"></div>
      <div class="chair-photo" role="img" aria-label="Photograph of an empty wooden rocking chair, front view"></div>
      <h1 class="cover-line title-top">BREATHE</h1>
      <div class="cover-line title-amp">&amp;</div>
      <div class="cover-line title-bottom">BLOOM</div>
      <p class="cover-line subtitle">UNMASKING PRICING MYTHS</p>
      <p class="cover-line author">MARK DELWITT</p>
    </article>
  </main>
</body>
</html>
```